AI Discovery Workshop Presentation

We have a wireframe presentation with 43 slides (many with the same format) to be implemented in Powerpoint. We provide Corporate presentation in order to reuse template. Please, be creative and don't take the examples in the wireframe as literal. We also provide the following:
- Color palette
- bytefolk Logos
- Slide wireframe
- Flyer
- bytefolk Corporate Presentation. Please, use this as a general template.
You can find all the materials here:
https://files.vantorbox.net/share/7QmZp2LxR9dKw4TnB8yHc3VfJ5sEaU0?usp=sharing

```html
<!DOCTYPE html>
<html lang="en">
<head>
<meta charset="utf-8">
<title>bytefolk – Technology Pitch Deck</title>
<link rel="stylesheet" href="https://fonts.googleapis.com/css2?family=Poppins:ital,wght@0,300;0,400;0,500;0,600;0,700;1,400&display=swap">
<style>
  :root{
    --canvas:#e4e5e7;
    --teal:#13a19a;
    --cyan:#2cc6d2;
    --white:#ffffff;
    --muted:#c9d4e6;
    --slide-bg:linear-gradient(180deg,#10707a 0%,#123a70 32%,#0c1a3d 68%,#0a1430 100%);
    --tile-bg:linear-gradient(90deg,#2b4bb2 0%,#1f6fa5 55%,#14a39b 100%);
  }
  *{box-sizing:border-box;margin:0;padding:0}
  html,body{width:809px;height:1200px;overflow:hidden;background:var(--canvas)}
  body{position:relative;font-family:"Poppins",sans-serif;color:var(--white)}

  .slide{position:absolute;width:380px;height:208px;overflow:hidden;background:var(--slide-bg);box-shadow:0 14px 18px -10px rgba(0,0,0,.35)}
  .col-a{left:14px}.col-b{left:415px}
  .row-1{top:61px}.row-2{top:351px}.row-3{top:641px}.row-4{top:931px}

  .slide-title{position:absolute;left:0;right:0;text-align:center;font-weight:700;font-size:14px}

  /* cover */
  .cover-photo{position:absolute;inset:0;background:radial-gradient(circle at 30% 40%,#6a2d5a 0%,#163c5c 35%,#0b1c33 75%),#0b1c33}
  .brand{position:absolute;display:flex;align-items:center;gap:4px;font-weight:600;color:var(--white)}
  .brand-mark{display:inline-block;background:var(--teal)}
  .cover .brand{left:12px;top:20px;font-size:17px}
  .cover .brand-mark{width:9px;height:9px}
  .title-box{position:absolute;left:173px;top:66px;width:176px;height:76px;background:linear-gradient(90deg,rgba(28,150,170,.85),rgba(50,80,190,.85));padding:10px 16px}
  .title-box .light{font-weight:300;font-size:18px;line-height:1;letter-spacing:.3px}
  .title-box .bold{font-weight:700;font-size:19px;line-height:1.15}
  .title-box .lede{font-style:italic;font-size:5px;line-height:1.4;margin-top:5px;color:var(--muted)}
  .cover .url{position:absolute;left:22px;bottom:11px;font-size:8px}

  /* future */
  .portrait{position:absolute;left:35px;top:27px;width:114px;height:159px;background:linear-gradient(160deg,#9aa3a6,#3e4a50);border:1.5px solid var(--teal)}
  .future h2{position:absolute;left:170px;top:45px;font-size:14px;font-weight:700}
  .quote{position:absolute;left:170px;top:74px;width:122px;height:62px;border:1px solid rgba(180,120,200,.5);border-top:none;padding:7px 6px;font-size:4.6px;line-height:1.5;text-align:justify}
  .quote .cite{text-align:right;margin-top:3px}
  .quote-mark{position:absolute;font-size:10px;font-weight:700;line-height:1}

  /* about */
  .about h2{top:32px}
  .about .sub{position:absolute;top:51px;width:100%;text-align:center;font-size:8px;font-weight:600}
  .about-card{position:absolute;left:40px;top:76px;width:298px;height:57px;background:linear-gradient(90deg,#1a3d78,#13a09a);border-left:1px solid var(--cyan);display:flex;align-items:center;gap:10px;padding:0 16px 0 10px;font-size:5.6px;line-height:1.55;text-align:justify}
  .about-card p{width:220px}
  .city{position:absolute;left:40px;top:142px;width:298px;height:66px;background:linear-gradient(180deg,#1596a5 0%,#1b3f7a 55%,#4b1f5e 100%)}

  /* services */
  .services h2{top:26px}
  .tile{position:absolute;width:110px;height:45px;background:var(--tile-bg);display:flex;align-items:center;justify-content:space-between;padding:0 9px;font-size:8px;font-weight:600;line-height:1.3}
  .tile svg{flex:none}

  /* framework */
  .framework h2{top:26px}
  .grid{position:absolute;left:28px;top:60px;width:322px}
  .pillars{display:grid;grid-template-columns:repeat(3,1fr);gap:5px;margin-bottom:5px}
  .pillars div{border:1px solid var(--teal);height:24px;display:flex;align-items:center;justify-content:center;font-size:7px;font-weight:600}
  .layers{border:1px solid var(--teal);padding:2px;display:grid;grid-template-columns:70px repeat(4,1fr);gap:3px}
  .layers div{height:17px;display:flex;align-items:center;justify-content:center;text-align:center;font-size:5px;font-weight:600;line-height:1.1;border:1px solid var(--teal);background:#0b1838}
  .layers .lead{font-size:6.2px}
  .layers .fill{background:linear-gradient(90deg,#1a3c7c,#13a09a)}
  .span-2{grid-column:span 2}

  /* ai */
  .ai h2{top:26px}
  .step{position:absolute;width:68px;height:66px;border-radius:5px;background:linear-gradient(180deg,#2e4dad,#14a19a);display:flex;align-items:center;justify-content:center;text-align:center;font-size:5.8px;font-weight:600;line-height:1.3}
  .badge{position:absolute;width:21px;height:21px;border-radius:3px;background:#3556b8;border:1px solid var(--white);display:flex;align-items:center;justify-content:center}
  .link{position:absolute;height:0;border-top:1px dashed rgba(180,200,255,.5)}

  /* analytics */
  .analytics{background:linear-gradient(180deg,#0a1330 0%,#0b1a3c 60%,#0f6a78 100%)}
  .analytics h2{top:28px}
  .diamond{position:absolute;width:28px;height:28px;transform:rotate(45deg);border-radius:3px;background:linear-gradient(135deg,#2c4db0,#16a09a);display:flex;align-items:center;justify-content:center}
  .diamond svg{transform:rotate(-45deg)}
  .d-label{position:absolute;font-size:5.8px;font-weight:600;line-height:1.3}

  /* talent */
  .talent{background:linear-gradient(180deg,#0a1330 0%,#0c1b40 100%)}
  .talent h3{position:absolute;left:188px;top:22px;font-size:6.4px;font-weight:700;color:#36a6e6}
  .talent ul{position:absolute;left:188px;top:32px;list-style:none;font-size:5px;line-height:1.95}
  .talent li::before{content:"•";margin-right:4px}
  .talent h2{position:absolute;left:30px;top:108px;font-size:13px;font-weight:700;line-height:1.2}
  .talent p{position:absolute;left:31px;top:150px;width:140px;font-size:6.6px;font-weight:600;line-height:1.4}
  .team{position:absolute;left:192px;top:104px;width:160px;height:76px;background:linear-gradient(120deg,#8a6a52,#c9a888 55%,#6b5b55);border:1px solid #6a55b8}
</style>
</head>
<body>

<section class="slide cover col-a row-1">
  <div class="cover-photo" role="img" aria-label="Photo of a person looking at a glowing holographic interface"></div>
  <div class="brand"><span class="brand-mark"></span>bytefolk</div>
  <div class="title-box">
    <div class="light">TECHNOLOGY</div>
    <div class="bold">PITCH DECK</div>
    <div class="lede">Lorem Ipsum is simply dummy text of the printing and typesetting industry</div>
  </div>
  <div class="url">www.bytefolk.cloud</div>
</section>

<section class="slide future col-b row-1">
  <div class="portrait" role="img" aria-label="Black and white photo of a woman with holographic data panels"></div>
  <h2>The Future is Now</h2>
  <span class="quote-mark" style="left:175px;top:71px">“</span>
  <div class="quote">
    <p>Generative AI has the potential to add trillions of dollars in value to the global economy and accelerate productivity growth for individuals, businesses and the economy as a whole.</p>
    <p class="cite">— Halvorsen &amp; Partners</p>
  </div>
  <span class="quote-mark" style="left:280px;top:133px">”</span>
</section>

<section class="slide about col-a row-2">
  <h2 class="slide-title">About Us</h2>
  <div class="sub">Data Analytics &amp; AI for Nonconformists</div>
  <div class="about-card">
    <svg width="34" height="30" viewBox="0 0 34 30" fill="none" stroke="#fff" stroke-width="1.2"><path d="M12 10a4 4 0 0 1 8-1 3.5 3.5 0 1 1 1 7H12a3 3 0 0 1 0-6z"/><path d="M16 16v4M8 20h18M8 20v3M26 20v3"/><rect x="2" y="22" width="13" height="7"/><rect x="22" y="22" width="9" height="7"/></svg>
    <p>We are a leading Professional Services company specialized in the design and implementation of cutting edge technologies in Cloud, Data Analytics &amp; AI.</p>
  </div>
  <div class="city" role="img" aria-label="Photo of a night city skyline with glowing towers"></div>
</section>

<section class="slide services col-b row-2">
  <h2 class="slide-title">What We Do</h2>
  <div class="tile" style="left:69px;top:60px">Agentic AI
    <svg width="18" height="18" viewBox="0 0 18 18" fill="none" stroke="#fff" stroke-width="1.2"><circle cx="9" cy="8" r="5"/><path d="M5 17h8M9 13v4"/></svg></div>
  <div class="tile" style="left:198px;top:60px">AI Agents
    <svg width="18" height="18" viewBox="0 0 18 18" fill="none" stroke="#fff" stroke-width="1.2"><circle cx="9" cy="5" r="3"/><path d="M3 17c0-4 3-7 6-7s6 3 6 7"/></svg></div>
  <div class="tile" style="left:69px;top:126px">Advanced<br>Analytics &amp; ML
    <svg width="18" height="18" viewBox="0 0 18 18" fill="none" stroke="#fff" stroke-width="1.2"><path d="M2 17V11M6 17V8M10 17V12"/><circle cx="14" cy="5" r="3"/></svg></div>
  <div class="tile" style="left:198px;top:126px">Data Analytics<br>&amp; Visualization
    <svg width="18" height="18" viewBox="0 0 18 18" fill="none" stroke="#fff" stroke-width="1.2"><rect x="1" y="2" width="16" height="11"/><path d="M6 17h6M9 13v4M5 10V8M9 10V5M13 10V7"/></svg></div>
</section>

<section class="slide framework col-a row-3">
  <h2 class="slide-title">What We Do</h2>
  <div class="grid">
    <div class="pillars"><div>TALENT</div><div>METHODOLOGY</div><div>TECHNOLOGY</div></div>
    <div class="layers">
      <div class="lead fill">ACTIVATION</div><div class="fill">Agentic<br>AI</div><div class="fill">AI<br>Agents</div><div class="fill">Advanced<br>Analytics &amp; ML</div><div class="fill">Data Analytics &amp;<br>Visualization</div>
      <div class="lead">MANAGEMENT</div><div>APIS/TOOLS</div><div>Models</div><div class="span-2">Data</div>
      <div class="lead fill">INTEGRATION</div><div class="fill span-2">Connectors</div><div class="fill span-2">Data Ingestion</div>
      <div class="lead">IT ASSETS</div><div class="span-2">Applications</div><div class="span-2">Data Source</div>
    </div>
  </div>
</section>

<section class="slide ai col-b row-3">
  <h2 class="slide-title">AI</h2>
  <div class="link" style="left:104px;top:76px;width:20px"></div>
  <div class="link" style="left:187px;top:76px;width:20px"></div>
  <div class="link" style="left:270px;top:76px;width:20px"></div>
  <div class="step" style="left:36px;top:66px">AI<br>Discovery<br>Workshop</div>
  <div class="step" style="left:119px;top:80px">AI<br>Strategy &amp;<br>Design</div>
  <div class="step" style="left:202px;top:66px">AI<br>Implementation</div>
  <div class="step" style="left:285px;top:80px">AI<br>Governance</div>
  <div class="badge" style="left:59px;top:123px"><svg width="11" height="11" viewBox="0 0 11 11" fill="none" stroke="#fff"><circle cx="5" cy="5" r="3.5"/><path d="M8 8l2.5 2.5"/></svg></div>
  <div class="badge" style="left:142px;top:66px"><svg width="11" height="11" viewBox="0 0 11 11" fill="none" stroke="#fff"><path d="M1 10V6M4 10V3M7 10V5M10 10V1"/></svg></div>
  <div class="badge" style="left:225px;top:123px"><svg width="11" height="11" viewBox="0 0 11 11" fill="none" stroke="#fff"><circle cx="5.5" cy="5.5" r="4"/><path d="M3.5 5.5l1.5 1.5 2.5-3"/></svg></div>
  <div class="badge" style="left:308px;top:66px"><svg width="11" height="11" viewBox="0 0 11 11" fill="none" stroke="#fff"><path d="M5.5 1v9M2 3h7M2 3l-1 4h2zM9 3l-1 4h2z"/></svg></div>
</section>

<section class="slide analytics col-a row-4">
  <h2 class="slide-title">Data Analytics</h2>
  <div class="diamond" style="left:170px;top:69px"><svg width="14" height="14" viewBox="0 0 14 14" fill="none" stroke="#fff"><rect x="2" y="1" width="8" height="11"/><circle cx="9" cy="9" r="3"/></svg></div>
  <div class="diamond" style="left:146px;top:93px"><svg width="14" height="14" viewBox="0 0 14 14" fill="none" stroke="#fff"><rect x="1" y="2" width="12" height="8"/><path d="M5 13h4"/></svg></div>
  <div class="diamond" style="left:194px;top:93px"><svg width="14" height="14" viewBox="0 0 14 14" fill="none" stroke="#fff"><rect x="2" y="1" width="8" height="11"/><path d="M8 9l1.5 1.5L12 8"/></svg></div>
  <div class="diamond" style="left:170px;top:117px"><svg width="14" height="14" viewBox="0 0 14 14" fill="none" stroke="#fff"><rect x="1" y="1" width="12" height="12"/><path d="M4 10V7M7 10V4M10 10V6"/></svg></div>
  <div class="d-label" style="left:108px;top:64px;text-align:right">Data Analytics<br>Assessment</div>
  <div class="d-label" style="left:243px;top:86px">Data Analytics<br>Governance</div>
  <div class="d-label" style="left:81px;top:136px;text-align:right">Data Analytics<br>Strategy &amp; Design</div>
  <div class="d-label" style="left:219px;top:155px">Data Analytics<br>Implementation</div>
</section>

<section class="slide talent col-b row-4">
  <h3>How do we make it happen</h3>
  <ul>
    <li>Strict selection process</li>
    <li>Competitive pay for premier talent</li>
    <li>Exciting technologies and projects</li>
    <li>100% certification target in 6 months</li>
    <li>10% continuous learning investment (3x market average)</li>
    <li>Culture that draws in the best professionals</li>
  </ul>
  <h2>Exceptional<br>Talent</h2>
  <p>Work with highly Motivated Trained and Committed Industry Professionals.</p>
  <div class="team" role="img" aria-label="Photo of a smiling team working together at a laptop"></div>
</section>

</body>
</html>
```